Combined entities letterhead

Hi
We need to combine our two sister business's logos onto a letterhead for invoicing and they will need to come under the banner of Coolvane Systems Pty Ltd.
I have attached our current logos, a copy of our current letterheads for Cool Vane WA and Coolvane Systems Pty Ltd. The idea would be to have the Coolvane Systems logo on top (with the words incorporating) and the 2 sister businesses under it in the header, or something similar. Some of the wording may need to be changed as far as contact numbers and addresses but I just want to get the basics layout completed first.

```html
<!DOCTYPE html>
<html lang="en">
<head>
<meta charset="utf-8">
<title>Coolvane Systems Letterhead</title>
<link rel="stylesheet" href="https://fonts.googleapis.com/css2?family=Arimo:wght@400&family=Open+Sans:wght@400;700&display=swap">
<style>
  :root {
    --paper: #f6f4f5;
    --ink: #3f3f41;
    --ink-soft: #505052;
    --brand-blue: #1e4fa3;
    --footer-ink: #2c2c2e;
    --sign-fill: #d9d8dc;
  }
  * { margin: 0; padding: 0; box-sizing: border-box; }
  html, body { width: 935px; height: 1200px; overflow: hidden; background: var(--paper); }
  .letterhead { position: relative; width: 935px; height: 1200px; background: var(--paper); color: var(--ink); font-family: "Arimo", Arial, sans-serif; }

  .brand { position: absolute; left: 93px; top: 124px; font-family: "Open Sans", sans-serif; font-weight: 700; color: var(--brand-blue); }
  .brand-name { font-size: 24px; line-height: 30px; }
  .brand-sister { margin: 20px 0 0 40px; font-size: 15px; line-height: 20px; }

  .company-details { position: absolute; left: 676px; top: 111px; font-family: "Open Sans", sans-serif; font-size: 11.5px; line-height: 16px; color: var(--footer-ink); }
  .company-details .gap { margin-left: 16px; }
  .company-details address { font-style: normal; margin-top: 5px; }
  .company-details .web { font-weight: 700; letter-spacing: 1.3px; }

  .salutation { position: absolute; left: 93px; top: 307px; font-size: 24px; color: var(--ink-soft); }

  .letter-body { position: absolute; left: 93px; top: 377px; width: 753px; font-size: 15px; line-height: 20.5px; text-align: justify; hyphens: auto; color: var(--ink); }
  .letter-body p { margin-bottom: 20px; }

  .sign-off { position: absolute; left: 93px; top: 829px; font-size: 15px; }
  .signature { position: absolute; left: 90px; top: 862px; width: 122px; height: 42px; background: var(--sign-fill); border-radius: 3px; }
  .signatory { position: absolute; left: 97px; top: 925px; }
  .signatory-name { font-size: 20px; color: var(--ink-soft); }
  .signatory-role { font-size: 15.5px; margin-top: 2px; }

  .footer { position: absolute; left: 38px; top: 1069px; width: 880px; font-family: "Open Sans", sans-serif; font-size: 12.5px; color: var(--footer-ink); }
  .footer-company { line-height: 17px; }
  .footer-head { font-weight: 700; line-height: 17px; }
  .offices { display: flex; margin-top: 1px; }
  .office { line-height: 18px; }
  .office:nth-child(1) { width: 183px; }
  .office:nth-child(2) { width: 240px; margin-top: 2px; }
  .office:nth-child(3) { width: 232px; margin-top: 2px; }
  .office:nth-child(4) { margin-top: 2px; }
  .office-name { font-weight: 700; }
  .contact { display: flex; align-items: center; gap: 7px; }
  .contact svg { width: 11px; height: 11px; fill: var(--brand-blue); flex: none; }
</style>
</head>
<body>
<main class="letterhead">
  <header>
    <div class="brand">
      <div class="brand-name">Cool Vane WA</div>
      <div class="brand-sister">Kelvin Airconditioning</div>
    </div>
    <div class="company-details">
      <div>ABN 42 518 730216</div>
      <div>AU51720<span class="gap">EC28403</span></div>
      <address>27 Marlin Street Geraldton<br>WA 6530</address>
      <div class="web">www.coolvane.com.au</div>
    </div>
  </header>

  <p class="salutation">Dear Mr. Smith,</p>

  <section class="letter-body">
    <p>Lorem ipsum dolor sit amet, consectetur adipiscing elit. Donec orci purus, luctus vitae dignissim eu, iaculis sed purus. Vivamus faucibus, ipsum nec aliquet viverra, leo mauris condimentum ligula, sit amet sagittis enim ligula quis arcu. Nam egestas tortor id nisi porttitor mattis. In tortor ante, ultricies in suscipit a, tempus non massa. Vivamus et auctor mi. Fusce vel massa nulla. Phasellus nec eros mauris, et scelerisque orci.</p>
    <p>Donec malesuada orci vitae nulla accumsan porta a id massa. Quisque accumsan iaculis magna sit amet fringilla. Maecenas consequat, magna eget tincidunt semper, odio nibh rutrum mi, id feugiat ante nisi eu risus. Vestibulum nunc orci, rhoncus a placerat in, ultricies in mi. Cras mattis varius eros, vel fringilla nisi suscipit eget. Quisque scelerisque sagittis nulla at porttitor.</p>
    <p>Sed id augue vitae urna euismod commodo aliquet a quam. Pellentesque arcu velit, cursus et malesuada ut, consequat et diam. Nullam erat sem, rhoncus id ullamcorper vitae, rhoncus et arcu. In ultricies ultricies nulla, ut rutrum nisi iaculis at. Donec eu magna a metus ornare faucibus. Fusce aliquet faucibus ultricies. Morbi semper, est id tincidunt gravida, sem arcu adipiscing lacus, ac bibendum nulla leo eu purus. Quisque nec diam sed risus consectetur a ccumsan quis quis nibh. Vestibulum id purus lorem.</p>
    <p>It is a long established fact that a reader will be distracted by the readable content of a page when looking at its layout. The point of using Lorem Ipsum is that it has a more-or-less normal distribution of letters, as opposed to using 'Content here, content here', making it look like readable English. Many desktop publishing packages</p>
  </section>

  <p class="sign-off">Sincerely,</p>
  <div class="signature" role="img" aria-label="Handwritten signature of John Smith"></div>
  <div class="signatory">
    <div class="signatory-name">John smith</div>
    <div class="signatory-role">CEO/ Founder</div>
  </div>

  <footer class="footer">
    <div class="footer-company">Coolvane Systems Pty Ltd</div>
    <div class="footer-head">Head office</div>
    <div class="offices">
      <div class="office">
        <div class="office-name">Geraldton</div>
        <div class="contact"><svg viewBox="0 0 24 24"><path d="M6.6 10.8a15.1 15.1 0 0 0 6.6 6.6l2.2-2.2a1 1 0 0 1 1-.25 11.4 11.4 0 0 0 3.6.57 1 1 0 0 1 1 1V20a1 1 0 0 1-1 1A17 17 0 0 1 3 4a1 1 0 0 1 1-1h3.5a1 1 0 0 1 1 1c0 1.25.2 2.45.57 3.57a1 1 0 0 1-.25 1z"/></svg>(08) 9900 1111</div>
        <div class="contact"><svg viewBox="0 0 24 24"><path d="M2 5h20v14H2zm2 2v.4l8 5.6 8-5.6V7z"/></svg>info@coolvane.com.au</div>
      </div>
      <div class="office">
        <div class="office-name">Pilbara</div>
        <div class="contact"><svg viewBox="0 0 24 24"><path d="M6.6 10.8a15.1 15.1 0 0 0 6.6 6.6l2.2-2.2a1 1 0 0 1 1-.25 11.4 11.4 0 0 0 3.6.57 1 1 0 0 1 1 1V20a1 1 0 0 1-1 1A17 17 0 0 1 3 4a1 1 0 0 1 1-1h3.5a1 1 0 0 1 1 1c0 1.25.2 2.45.57 3.57a1 1 0 0 1-.25 1z"/></svg>(08) 9100 2222</div>
        <div class="contact"><svg viewBox="0 0 24 24"><path d="M2 5h20v14H2zm2 2v.4l8 5.6 8-5.6V7z"/></svg>pilbaraadmin@coolvane.com.au</div>
      </div>
      <div class="office">
        <div class="office-name">Meekatharra</div>
        <div class="contact"><svg viewBox="0 0 24 24"><path d="M6.6 10.8a15.1 15.1 0 0 0 6.6 6.6l2.2-2.2a1 1 0 0 1 1-.25 11.4 11.4 0 0 0 3.6.57 1 1 0 0 1 1 1V20a1 1 0 0 1-1 1A17 17 0 0 1 3 4a1 1 0 0 1 1-1h3.5a1 1 0 0 1 1 1c0 1.25.2 2.45.57 3.57a1 1 0 0 1-.25 1z"/></svg>(08) 9900 3333</div>
        <div class="contact"><svg viewBox="0 0 24 24"><path d="M2 5h20v14H2zm2 2v.4l8 5.6 8-5.6V7z"/></svg>meekaadmin@coolvane.com.au</div>
      </div>
      <div class="office">
        <div class="office-name">Perth</div>
        <div class="contact"><svg viewBox="0 0 24 24"><path d="M6.6 10.8a15.1 15.1 0 0 0 6.6 6.6l2.2-2.2a1 1 0 0 1 1-.25 11.4 11.4 0 0 0 3.6.57 1 1 0 0 1 1 1V20a1 1 0 0 1-1 1A17 17 0 0 1 3 4a1 1 0 0 1 1-1h3.5a1 1 0 0 1 1 1c0 1.25.2 2.45.57 3.57a1 1 0 0 1-.25 1z"/></svg>(08) 9200 4444</div>
        <div class="contact"><svg viewBox="0 0 24 24"><path d="M2 5h20v14H2zm2 2v.4l8 5.6 8-5.6V7z"/></svg>perthadmin@coolvane.com.au</div>
      </div>
    </div>
  </footer>
</main>
</body>
</html>
```